A 'new law' boutique Australian law firm that provides specialist employment law and people managem

We value helping clients create results with respect workplaces. What differentiates us is we provide actionable training in understanding and dealing with people and ensure legal compliance fits with this approach. We would like a fresh approach to our training overview documents that we currently use in our current law firm (6 attached). Please use pictures, symbols etc consistent with our non-traditional law approach that captures the approach of each training session.. Attached is the logo and draft letterhead for Brook Legal which will launch soon.

Target Market(s)

HR Managers and in-house lawyers (non employment specialists) in mid-large Australian companies that are progressive with a relationship based approach to managing employee behaviours and disputes.

Industry/Entity Type

Human Resource

Font styles to use
Sans Serif

Colors
3176b5
33a6d7

Requirements
Must have
• 1 or 2 page PDF for each of the 6 documents that the wording supplied goes into your design which will be pretty similar as we want consistency with our documents

```html
<!DOCTYPE html>
<html lang="en">
<head>
<meta charset="utf-8">
<title>Brook Legal – Contact Officer Training</title>
<link href="https://fonts.googleapis.com/css2?family=Open+Sans:wght@400;600;700&display=swap" rel="stylesheet">
<style>
  :root{
    --bg:#e4e3e2;
    --paper:#ffffff;
    --grey:#d6d4d2;
    --grey-dark:#8d8a87;
    --brand-blue:#3176b5;
    --sky:#33a6d7;
    --lime:#b0ae32;
    --olive:#8e8b2a;
    --teal:#2a7d87;
    --teal-dark:#1f6670;
    --taupe:#5e5651;
    --ink:#3a3a3a;
    --white:#ffffff;
  }
  *{box-sizing:border-box;margin:0;padding:0}
  html,body{width:1200px;height:802px;overflow:hidden}
  body{background:var(--bg);font-family:"Open Sans",sans-serif;color:var(--ink);position:relative}
  .page{position:absolute;top:46px;width:500px;height:710px;background:var(--paper);overflow:hidden;box-shadow:0 2px 10px rgba(0,0,0,.12)}
  .page--overview{left:70px}
  .page--outcomes{left:630px}

  /* page 1 */
  .masthead{position:absolute;left:0;top:0;width:500px;height:100px;background:var(--grey)}
  .brand{position:absolute;left:30px;top:30px;font-weight:600;font-size:21px;color:var(--ink)}
  .brand__tag{position:absolute;left:30px;top:62px;font-size:8px;color:var(--grey-dark);letter-spacing:1px;text-transform:uppercase}
  .accent-stripes{position:absolute;left:248px;top:70px;display:flex;gap:3px;z-index:2}
  .accent-stripes span{width:7px;height:80px}
  .accent-stripes .s1{background:var(--sky)}
  .accent-stripes .s2{background:var(--teal)}
  .accent-stripes .s3{background:var(--sky)}
  .title-block{position:absolute;left:285px;top:95px;width:215px;height:55px;background:var(--lime);z-index:2;display:flex;align-items:center;padding-left:16px}
  .title-block h1{font-size:15px;font-weight:600;color:var(--white)}
  .hero{position:absolute;left:130px;top:110px;width:370px;height:160px;background:linear-gradient(135deg,#d9dadc 0%,#7b8592 45%,#2c3545 100%)}
  .needs{position:absolute;left:0;top:150px;width:172px;height:440px;background:var(--sky);color:var(--white);padding:14px 14px;z-index:1}
  .needs h2{font-size:12px;font-weight:700;color:var(--white);margin-bottom:8px}
  .needs p{font-size:9.5px;line-height:1.45;margin-bottom:9px}
  .outcomes{position:absolute;left:190px;top:278px;width:292px}
  .outcomes h2{font-size:13px;font-weight:600;color:var(--sky);margin-bottom:6px}
  .outcomes__intro{font-size:9.5px;line-height:1.4;margin-bottom:10px}
  .outcome-list{list-style:none}
  .outcome-list li{display:flex;gap:10px;align-items:flex-start;font-size:9.5px;line-height:1.35;padding:6px 0;border-bottom:1px solid #e6e6e6}
  .outcome-list svg{flex:0 0 16px}

  /* page 2 */
  .top-band{position:absolute;left:0;top:0;width:500px;height:48px;background:var(--grey)}
  .top-band h2{position:absolute;left:158px;top:22px;font-size:13px;font-weight:600;color:var(--brand-blue)}
  .topics{position:absolute;left:0;top:48px;width:500px}
  .topic{display:flex}
  .topic__label{width:148px;display:flex;align-items:center;justify-content:center;text-align:center;font-size:11.5px;font-weight:700;color:var(--white);padding:0 10px;line-height:1.2}
  .topic__text{flex:1;display:flex;align-items:center;padding:6px 14px;font-size:9.5px;line-height:1.38;color:var(--white)}
  .label--sky{background:var(--sky)}
  .label--lime{background:var(--lime)}
  .label--teal{background:var(--teal)}
  .label--taupe{background:var(--taupe)}
  .label--grey{background:var(--grey-dark)}
  .band--teal{background:var(--teal)}
  .band--olive{background:var(--olive)}
  .band--deep{background:var(--teal-dark)}
  .band--taupe{background:var(--taupe)}
  .band--plain{background:var(--paper);color:var(--ink)!important}
  .contact-foot{position:absolute;left:0;top:560px;width:500px;height:150px}
  .contact-foot svg.bg{position:absolute;left:0;top:0}
  .online{position:absolute;left:26px;top:18px;list-style:none;color:var(--white);font-size:9.5px}
  .online li,.offices li{display:flex;align-items:center;gap:7px;margin-bottom:5px}
  .dot{width:11px;height:11px;border-radius:50%;background:var(--white);flex:0 0 11px}
  .offices{position:absolute;right:22px;top:62px;list-style:none;color:var(--white);font-size:9.5px;text-align:right}
  .offices li{justify-content:flex-end}
  .offices .dot{background:var(--brand-blue)}
</style>
</head>
<body>

<section class="page page--overview">
  <header class="masthead">
    <div class="brand">Brook Legal</div>
    <div class="brand__tag">Employment Law &amp; People Management</div>
  </header>
  <div class="accent-stripes"><span class="s1"></span><span class="s2"></span><span class="s3"></span></div>
  <div class="title-block"><h1>Contact Officer Training</h1></div>
  <div class="hero" role="img" aria-label="Photograph of a professional in a suit gesturing during a workplace discussion"></div>

  <aside class="needs">
    <h2>Training Needs</h2>
    <p>Unlawful or inappropriate behaviour in the workplace can damage morale, productivity and trust. Contact Officers are often the first point of call and need the skills to respond early and well.</p>
    <p>Clear policies and procedures support the organisation's obligations and show staff that concerns will be handled fairly.</p>
    <p>The challenge is ensuring that Contact Officers understand the behaviours which breach the law and policy, and know how to guide staff through the available options.</p>
    <p>Well trained Contact Officers provide practical support to prevent and resolve issues in a respectful workplace.</p>
  </aside>

  <section class="outcomes">
    <h2>Learning Outcomes</h2>
    <p class="outcomes__intro">Training will enable participants to perform their role of Contact Officer and to understand:</p>
    <ul class="outcome-list">
      <li><svg width="16" height="14" viewBox="0 0 16 14"><polygon points="0,0 16,7 0,14" fill="#33a6d7"/></svg>The role and responsibilities of a Contact Officer</li>
      <li><svg width="16" height="14" viewBox="0 0 16 14"><polygon points="0,0 16,7 0,14" fill="#b0ae32"/></svg>What amounts to unlawful workplace behaviour</li>
      <li><svg width="16" height="14" viewBox="0 0 16 14"><polygon points="0,0 16,7 0,14" fill="#5e5651"/></svg>What is considered inappropriate behaviour</li>
      <li><svg width="16" height="14" viewBox="0 0 16 14"><polygon points="0,0 16,7 0,14" fill="#2a7d87"/></svg>How to apply understanding unlawful/inappropriate behaviour in our workplace to common scenarios</li>
      <li><svg width="16" height="14" viewBox="0 0 16 14"><polygon points="0,0 16,7 0,14" fill="#33a6d7"/></svg>How to address and resolve grievances early</li>
      <li><svg width="16" height="14" viewBox="0 0 16 14"><polygon points="0,0 16,7 0,14" fill="#b0ae32"/></svg>Options to resolve grievances internally and the Contact Officer role</li>
      <li><svg width="16" height="14" viewBox="0 0 16 14"><polygon points="0,0 16,7 0,14" fill="#5e5651"/></svg>External options and their pros and cons for resolving grievances</li>
    </ul>
  </section>
</section>

<section class="page page--outcomes">
  <header class="top-band"><h2>Outcome</h2></header>
  <div class="topics">
    <div class="topic" style="height:68px"><div class="topic__label label--sky">Discrimination</div><div class="topic__text band--teal">What is direct and indirect discrimination? What are the protected attributes? What are the exceptions to the general prohibition? Examples of behaviour that may be discriminatory.</div></div>
    <div class="topic" style="height:82px"><div class="topic__label label--lime">Harassment</div><div class="topic__text band--olive">What is harassment? Are protected attributes relevant to harassment? What is the difference between harassment and sexual harassment? How does the reasonable person test apply? Practical examples of behaviour that may be harassment or sexual harassment.</div></div>
    <div class="topic" style="height:62px"><div class="topic__label label--teal">Bullying</div><div class="topic__text band--deep">What is bullying? Explore how bullying differs to harassment and discrimination. Reasonable management action – is it still bullying? Practical examples of conduct that may be bullying.</div></div>
    <div class="topic" style="height:44px"><div class="topic__label label--taupe">Victimisation &amp; Vilification</div><div class="topic__text band--taupe">What is victimisation? What is vilification?</div></div>
    <div class="topic" style="height:74px"><div class="topic__label label--sky">Adverse Action</div><div class="topic__text band--teal">What is adverse action and how does it differ to other unlawful behaviour? What is a workplace right? When is it unlawful to terminate employment because of an employee's absence? How are the protected attributes relevant to adverse action?</div></div>
    <div class="topic" style="height:54px"><div class="topic__label label--lime">The Contact Officer's role</div><div class="topic__text band--olive">How to perform your role when approached by an employee – the 5 step approach. What not to do. What are the obligations with regard to confidentiality?</div></div>
    <div class="topic" style="height:88px"><div class="topic__label label--teal">Grievance Options</div><div class="topic__text band--deep">Explore the options of complaint management – self management, internal informal management, formal internal management. How do they compare and what are the advantages and disadvantages? External options – each approach. Is doing nothing an option? Who decides which option?</div></div>
    <div class="topic" style="height:40px"><div class="topic__label label--grey">Test Learning</div><div class="topic__text band--plain">Role play, group discussion</div></div>
  </div>

  <footer class="contact-foot">
    <svg class="bg" width="500" height="150" viewBox="0 0 500 150"><rect width="500" height="150" fill="#8d8a87"/><polygon points="0,0 500,0 500,8 240,150 0,150" fill="#3176b5"/></svg>
    <ul class="online">
      <li><span class="dot"></span>@brooklegal</li>
      <li><span class="dot"></span>@brooklegal</li>
      <li><span class="dot"></span>www.brooklegal.com.au</li>
      <li><span class="dot"></span>hello@brooklegal.com.au</li>
    </ul>
    <ul class="offices">
      <li>41 Harbour Lane<br>Hobart 7000 <span class="dot"></span></li>
      <li>(03) 6200 0000 <span class="dot"></span></li>
      <li>12 Ridge St, Melbourne 3000 <span class="dot"></span></li>
      <li>(03) 9400 0000 <span class="dot"></span></li>
    </ul>
  </footer>
</section>

</body>
</html>
```